Lanternleaf - Fresh Asian Cuisine Menu

We need to redo our menu to include pictures of food items. Our restaurant is vibrant, trendy, upscale Chinese cuisine

Requirements
Must have
• Must fit on 8.5x11 paper. We can remove the About Us section if needed but menu cannot be more than 6 pages total. Must include pictures of menu items

```html
<!DOCTYPE html>
<html lang="en">
<head>
<meta charset="utf-8">
<title>Lanternleaf - Fresh Asian Cuisine · Entrees</title>
<link rel="stylesheet" href="https://fonts.googleapis.com/css2?family=Passion+One:wght@400;700&family=Titan+One&family=Alegreya+SC:wght@700&family=Archivo+Narrow:wght@600&family=Hind:wght@600&display=swap">
<style>
  :root {
    --maroon: #6b1a1c;
    --bar: #5a1517;
    --red: #d9252c;
    --green: #4aa83f;
    --ink: #1d1d1d;
    --paper: #ffffff;
  }
  html, body { margin: 0; padding: 0; overflow: hidden; }
  body { width: 927px; height: 1200px; background: var(--paper); }
  .menu {
    position: relative; width: 927px; height: 1200px; overflow: hidden;
    background: var(--paper); font-family: "Archivo Narrow", "Arial Narrow", sans-serif; color: var(--ink);
  }
  .rule { position: absolute; height: 4px; background: var(--red); }
  .rule--top { left: 0; top: 40px; width: 680px; }
  .rule--bottom { left: 236px; top: 1166px; width: 691px; }

  .brand { position: absolute; display: flex; flex-direction: column; align-items: flex-start; }
  .brand--top { left: 690px; top: 28px; }
  .brand--bottom { left: 30px; top: 1146px; }
  .brand__row { display: flex; align-items: center; gap: 6px; }
  .brand__name {
    font-family: "Passion One", Arial, sans-serif; font-weight: 700;
    font-size: 34px; line-height: 30px; color: var(--ink); letter-spacing: 0.5px;
  }
  .brand__dot { width: 14px; height: 14px; border-radius: 50%; background: var(--red); }
  .brand__tag {
    font-family: "Hind", Arial, sans-serif; font-weight: 600; font-size: 8.5px;
    letter-spacing: 1.6px; color: var(--red); margin-top: 1px; margin-left: 2px;
  }

  .page-title {
    position: absolute; left: 0; width: 927px; top: 50px; margin: 0; text-align: center;
    font-family: "Passion One", Arial, sans-serif; font-weight: 700; font-size: 54px;
    color: var(--maroon); letter-spacing: 1px; padding-right: 10px; box-sizing: border-box;
  }
  .section-title {
    position: absolute; margin: 0; font-family: "Titan One", Arial, sans-serif;
    font-weight: 400; font-size: 25px; color: var(--paper);
    -webkit-text-stroke: 1.6px var(--maroon); letter-spacing: 0.5px;
  }
  .section-title--beef { left: 150px; top: 110px; }
  .section-title--chef { left: 566px; top: 110px; }
  .section-title--green {
    left: 600px; top: 953px; color: var(--green); -webkit-text-stroke: 0;
    font-family: "Passion One", Arial, sans-serif; font-weight: 700; font-size: 28px;
  }

  .dish { position: absolute; height: 150px; }
  .dish--left { left: 27px; width: 442px; }
  .dish--right { left: 477px; width: 439px; }
  .dish__bar {
    height: 20px; background: var(--bar); color: var(--paper);
    font-family: "Alegreya SC", Georgia, serif; font-weight: 700; font-size: 14px;
    line-height: 21px; padding-left: 6px; letter-spacing: 0.3px;
  }
  .dish__photo { width: 196px; height: 128px; }
  .dish__price {
    position: absolute; top: 0; width: 62px; height: 62px; border-radius: 50%;
    background: var(--red); color: var(--paper); display: flex; align-items: center;
    justify-content: center; font-family: "Passion One", Arial, sans-serif;
    font-size: 29px; letter-spacing: 0.5px;
  }
  .dish--left .dish__price { left: 357px; }
  .dish--right .dish__price { left: 359px; }
  .dish__price sup { font-size: 17px; margin-right: 1px; position: relative; top: -2px; }
  .dish__heat { position: absolute; top: 27px; left: 200px; display: flex; gap: 3px; }
  .dish__desc {
    position: absolute; left: 200px; margin: 0; font-size: 12px; font-weight: 600;
    line-height: 15px;
  }
  .dish__desc--top { top: 24px; width: 150px; }
  .dish__desc--under-heat { top: 66px; width: 200px; }
  .dish--right .dish__desc--under-heat { width: 222px; }
  .chili { width: 30px; height: 22px; }
</style>
</head>
<body>
<main class="menu">
  <svg width="0" height="0" style="position:absolute">
    <defs>
      <symbol id="chili-icon" viewBox="0 0 30 22">
        <path d="M24 6c2-2 4-3 5-5" stroke="#3f8a2e" stroke-width="2" fill="none" stroke-linecap="round"/>
        <path d="M23 6c-3-1-6 0-8 3C11 15 6 18 1 19c5 2 12 1 17-4 4-4 7-6 5-9z" fill="#d9252c"/>
      </symbol>
    </defs>
  </svg>

  <div class="rule rule--top"></div>
  <div class="brand brand--top">
    <div class="brand__row"><span class="brand__name">LANTERNLEAF</span><span class="brand__dot"></span></div>
    <span class="brand__tag">FRESH ASIAN CUISINE</span>
  </div>

  <h1 class="page-title">ENTREES</h1>
  <h2 class="section-title section-title--beef">BEEF &amp; PORK</h2>
  <h2 class="section-title section-title--chef">CHEF SPECIALTIES</h2>

  <!-- Beef & Pork column -->
  <article class="dish dish--left" style="top:153px">
    <div class="dish__bar">Dancing Beef</div>
    <div class="dish__photo" role="img" aria-label="Photo of dancing beef on sizzling rice crackers" style="background:radial-gradient(circle at 50% 50%,#c8532e 0,#a34426 30%,#efe9e2 55%,#8d8f95 100%)"></div>
    <div class="dish__heat"><svg class="chili"><use href="#chili-icon"/></svg><svg class="chili"><use href="#chili-icon"/></svg><svg class="chili"><use href="#chili-icon"/></svg></div>
    <p class="dish__desc dish__desc--under-heat">Angus Beef slices on a bed of sizzling rice crackers, black peppercorn and Thai chili</p>
    <div class="dish__price"><sup>$</sup>16</div>
  </article>

  <article class="dish dish--left" style="top:316px">
    <div class="dish__bar">Oyster Beef</div>
    <div class="dish__photo" role="img" aria-label="Photo of oyster beef with onions" style="background:radial-gradient(circle at 50% 50%,#4a2a1c 0,#5c3322 22%,#e8e4de 40%,#8a7f72 100%)"></div>
    <p class="dish__desc dish__desc--top">Tender cuts of steak wok fried with onions and marinated in a homemade oyster sauce</p>
    <div class="dish__price"><sup>$</sup>14</div>
  </article>

  <article class="dish dish--left" style="top:481px">
    <div class="dish__bar">Double Pepper Beef</div>
    <div class="dish__photo" role="img" aria-label="Photo of double pepper beef in chili broth" style="background:radial-gradient(circle at 50% 50%,#b3261c 0,#9c2518 35%,#e6dfd4 52%,#a89a86 100%)"></div>
    <div class="dish__heat"><svg class="chili"><use href="#chili-icon"/></svg><svg class="chili"><use href="#chili-icon"/></svg><svg class="chili"><use href="#chili-icon"/></svg></div>
    <p class="dish__desc dish__desc--under-heat">Angus steak with peppercorn, Thai chili, Serrano pepper and tofu and rice noodles</p>
    <div class="dish__price"><sup>$</sup>16</div>
  </article>

  <article class="dish dish--left" style="top:646px">
    <div class="dish__bar">Black Pepper Steak</div>
    <div class="dish__photo" role="img" aria-label="Photo of black pepper steak in a skillet" style="background:radial-gradient(ellipse at 50% 55%,#4b3a2c 0,#2b2522 40%,#3b3d40 70%,#5c5d60 100%)"></div>
    <div class="dish__heat"><svg class="chili"><use href="#chili-icon"/></svg></div>
    <p class="dish__desc dish__desc--under-heat">Tender cuts of steak mixed with onions and red and green bell peppers</p>
    <div class="dish__price"><sup>$</sup>15</div>
  </article>

  <article class="dish dish--left" style="top:810px">
    <div class="dish__bar">Singapore Baby Back Ribs</div>
    <div class="dish__photo" role="img" aria-label="Photo of glazed baby back ribs with bok choy" style="background:radial-gradient(circle at 50% 50%,#3d2414 0,#4a2c18 25%,#e9e6e1 45%,#7d7a76 100%)"></div>
    <p class="dish__desc dish__desc--top" style="top:21px">Tender Baby back ribs rubbed in a Thai inspired sweet tangy glaze</p>
    <div class="dish__price"><sup>$</sup>16</div>
  </article>

  <article class="dish dish--left" style="top:974px">
    <div class="dish__bar">Dancing Pork Belly</div>
    <div class="dish__photo" role="img" aria-label="Photo of braised pork belly on rice cracker with broccoli" style="background:radial-gradient(ellipse at 45% 55%,#d9c9a2 0,#7a3a1e 35%,#e8e6e2 60%,#b9b5ae 100%)"></div>
    <p class="dish__desc dish__desc--top">Braised Pork Belly on sizzling rice cracker</p>
    <div class="dish__price"><sup>$</sup>15</div>
  </article>

  <!-- Chef Specialties column -->
  <article class="dish dish--right" style="top:153px">
    <div class="dish__bar">Jasmine Tea Smoked Duck</div>
    <div class="dish__photo" role="img" aria-label="Photo of tea smoked duck with steamed buns and cucumber" style="background:linear-gradient(135deg,#e9e6e0 0,#c9a27e 45%,#8a4a2a 70%,#5b5f66 100%)"></div>
    <p class="dish__desc dish__desc--top" style="top:22px">Boneless half duck served with thinly sliced cucumber, scallion, house made duck sauce and soft flour wrap</p>
    <div class="dish__price"><sup>$</sup>24</div>
  </article>

  <article class="dish dish--right" style="top:314px">
    <div class="dish__bar">Sizzling Cumin’ Lamb</div>
    <div class="dish__photo" role="img" aria-label="Photo of cumin lamb with peppers and onions" style="background:radial-gradient(circle at 50% 50%,#8c4a23 0,#a1542b 28%,#efebe5 48%,#8b8377 100%)"></div>
    <div class="dish__heat" style="top:34px"><svg class="chili"><use href="#chili-icon"/></svg></div>
    <p class="dish__desc dish__desc--under-heat">Tender pieces of lamb rubbed in cumin, Sichuan peppers, red and green bell peppers and onions</p>
    <div class="dish__price" style="top:4px"><sup>$</sup>16</div>
  </article>

  <article class="dish dish--right" style="top:476px">
    <div class="dish__bar">Chef Lin’s Spicy Fish</div>
    <div class="dish__photo" role="img" aria-label="Photo of spicy fish fillet in peppercorn sauce" style="background:radial-gradient(circle at 50% 50%,#c25a2c 0,#b2461f 35%,#ebe5dc 55%,#9c907f 100%)"></div>
    <div class="dish__heat"><svg class="chili"><use href="#chili-icon"/></svg><svg class="chili"><use href="#chili-icon"/></svg></div>
    <p class="dish__desc dish__desc--under-heat">Fish filet in house made green peppercorn sauce with Chinese cabbage, sprouts and celery garnished with fresh Sichuan peppercorn, Thai chili and cilantro</p>
    <div class="dish__price"><sup>$</sup>17</div>
  </article>

  <article class="dish dish--right" style="top:638px">
    <div class="dish__bar">General Tso’s Scallops</div>
    <div class="dish__photo" role="img" aria-label="Photo of glazed scallops with broccoli" style="background:radial-gradient(circle at 50% 45%,#5a2f1a 0,#3f6b2a 30%,#ece9e4 50%,#a49a8d 100%)"></div>
    <div class="dish__heat" style="top:34px"><svg class="chili"><use href="#chili-icon"/></svg></div>
    <p class="dish__desc dish__desc--under-heat" style="top:68px">The perfect combination of tender scallops marinated in a sweet chili sauce with broccoli and red peppersv</p>
    <div class="dish__price"><sup>$</sup>18</div>
  </article>

  <article class="dish dish--right" style="top:798px">
    <div class="dish__bar">Chef Lin’s Spicy Beef</div>
    <div class="dish__photo" role="img" aria-label="Photo of spicy beef in peppercorn sauce" style="background:radial-gradient(circle at 50% 50%,#a8401c 0,#8f3a1d 28%,#3c3633 50%,#5a5452 100%)"></div>
    <div class="dish__heat"><svg class="chili"><use href="#chili-icon"/></svg><svg class="chili"><use href="#chili-icon"/></svg></div>
    <p class="dish__desc dish__desc--under-heat">Angus beef in house made green peppercorn sauce with Chinese cabbage, sprouts and celery garnished with fresh Sichuan peppercorn, Thai chili and cilantrov</p>
    <div class="dish__price"><sup>$</sup>16</div>
  </article>

  <h2 class="section-title section-title--green">BEEF &amp; PORK</h2>

  <article class="dish dish--right" style="top:998px">
    <div class="dish__bar">Twice Cooked Pork</div>
    <div class="dish__photo" role="img" aria-label="Photo of twice cooked pork belly with leek" style="background:radial-gradient(circle at 50% 50%,#b07a48 0,#9a6236 30%,#e7e2da 55%,#5a5c61 100%)"></div>
    <div class="dish__heat" style="top:34px"><svg class="chili"><use href="#chili-icon"/></svg></div>
    <p class="dish__desc dish__desc--under-heat" style="top:70px">Stir fried Pork Belly slices with leek and fermented black beans</p>
    <div class="dish__price" style="top:5px"><sup>$</sup>14</div>
  </article>

  <div class="rule rule--bottom"></div>
  <div class="brand brand--bottom">
    <div class="brand__row"><span class="brand__name">LANTERNLEAF</span><span class="brand__dot"></span></div>
    <span class="brand__tag">FRESH ASIAN CUISINE</span>
  </div>
</main>
</body>
</html>
```